Vantrel - corporate Business Card

We need a good look and innovative business card for a new start up company based in Los Angeles called "Vantrel". We are in a payment business, including payment card, app, and ewallet. We are expert in online payment and Card not present (CNP) transaction.
We need an innovative, modern business card.

Our logo font is Aero Matics

Target Market(s)

Startup - Bank - Online Payment - Card Manufacturing

Industry/Entity Type

Startup

Contact Information for Business Card

phone: 555 371 6042 - Address: 4270 Marrowgate blvd, Dalmont City, CA 90418

Requirements
Must have
• Message: innovative, professional, expert, high tech, trust, online payment expert, security
Nice to have
• no comment
Should not have
• no Comment

```html
<!DOCTYPE html>
<html lang="en">
<head>
<meta charset="utf-8">
<title>Vantrel – Business Card</title>
<link rel="stylesheet" href="https://fonts.googleapis.com/css2?family=Roboto:wght@300;400;700&display=swap">
<style>
  :root {
    --brand-red: #b71f2e;
    --brand-red-dark: #9c1726;
    --paper: #ffffff;
    --ink: #4a4a4a;
    --muted: #8a8a8a;
    --rule: #9a9a9a;
    --backdrop: #e6e6e8;
  }
  * { box-sizing: border-box; margin: 0; padding: 0; }
  html, body {
    width: 1200px;
    height: 950px;
    overflow: hidden;
    background: var(--backdrop);
    font-family: "Roboto", sans-serif;
  }
  .sheet {
    width: 1200px;
    height: 950px;
    display: flex;
    flex-direction: column;
    align-items: center;
    justify-content: center;
    gap: 50px;
  }
  .card {
    position: relative;
    width: 700px;
    height: 400px;
    overflow: hidden;
    box-shadow: 0 6px 18px rgba(0,0,0,0.18);
  }

  /* Front */
  .card--front {
    background: var(--paper);
    border-bottom: 8px solid var(--brand-red);
  }
  .brand {
    position: absolute;
    top: 82px;
    left: 0;
    right: 0;
    display: flex;
    justify-content: center;
    align-items: center;
    gap: 14px;
  }
  .brand__dot {
    width: 58px;
    height: 58px;
    border-radius: 50%;
    background: var(--brand-red);
  }
  .brand__name {
    font-size: 60px;
    font-weight: 700;
    color: var(--brand-red);
    letter-spacing: 1px;
    line-height: 1;
  }
  .divider {
    position: absolute;
    top: 228px;
    left: 50px;
    right: 50px;
    height: 1px;
    background: var(--rule);
  }
  .person {
    position: absolute;
    left: 50px;
    top: 248px;
  }
  .person__name {
    font-size: 22px;
    font-weight: 400;
    color: var(--brand-red);
    line-height: 26px;
  }
  .person__role {
    font-size: 17px;
    font-weight: 300;
    color: var(--muted);
    line-height: 22px;
    margin-top: 2px;
  }
  .contacts {
    list-style: none;
    margin-top: 14px;
  }
  .contacts li {
    display: flex;
    align-items: center;
    gap: 10px;
    font-size: 16px;
    font-weight: 400;
    color: var(--ink);
    line-height: 22px;
  }
  .contacts svg { width: 14px; height: 14px; fill: var(--brand-red); flex: none; }
  .address {
    position: absolute;
    right: 50px;
    top: 250px;
    text-align: right;
    font-size: 17px;
    font-weight: 400;
    font-style: normal;
    color: var(--ink);
    line-height: 24px;
  }

  /* Back */
  .card--back {
    background: var(--brand-red);
    border-bottom: 8px solid var(--brand-red-dark);
  }
  .emblem {
    position: absolute;
    top: 50%;
    left: 50%;
    width: 230px;
    height: 230px;
    transform: translate(-50%, -50%);
    border-radius: 50%;
    background: var(--paper);
    display: flex;
    align-items: center;
    justify-content: center;
  }
  .emblem__name {
    font-size: 38px;
    font-weight: 700;
    color: var(--brand-red);
    letter-spacing: 1px;
  }
  .web {
    position: absolute;
    left: 40px;
    bottom: 40px;
    font-size: 14px;
    font-weight: 300;
    color: var(--paper);
    letter-spacing: 7px;
  }
</style>
</head>
<body>
<main class="sheet">
  <section class="card card--front" aria-label="Business card front">
    <div class="brand">
      <span class="brand__dot"></span>
      <span class="brand__name">vantrel</span>
    </div>
    <div class="divider"></div>
    <div class="person">
      <p class="person__name">Marla Kestin</p>
      <p class="person__role">President</p>
      <ul class="contacts">
        <li>
          <svg viewBox="0 0 24 24" aria-hidden="true"><path d="M6.6 10.8a15.1 15.1 0 0 0 6.6 6.6l2.2-2.2a1 1 0 0 1 1-.25 11.4 11.4 0 0 0 3.6.57 1 1 0 0 1 1 1V20a1 1 0 0 1-1 1A17 17 0 0 1 3 4a1 1 0 0 1 1-1h3.5a1 1 0 0 1 1 1c0 1.25.2 2.45.57 3.57a1 1 0 0 1-.25 1z"/></svg>
          555 371 6042
        </li>
        <li>
          <svg viewBox="0 0 24 24" aria-hidden="true"><path d="M7 1h10a2 2 0 0 1 2 2v18a2 2 0 0 1-2 2H7a2 2 0 0 1-2-2V3a2 2 0 0 1 2-2zm0 3v14h10V4z"/></svg>
          555 208 1937
        </li>
        <li>
          <svg viewBox="0 0 24 24" aria-hidden="true"><path d="M2 5h20v14H2zm2 2v.5l8 5 8-5V7z"/></svg>
          marla@vantrel.com
        </li>
      </ul>
    </div>
    <address class="address">4270 Marrowgate blvd<br>Dalmont City, CA 90418</address>
  </section>

  <section class="card card--back" aria-label="Business card back">
    <div class="emblem"><span class="emblem__name">vantrel</span></div>
    <p class="web">www.vantrel.ia</p>
  </section>
</main>
</body>
</html>
```